New Energy Drink

*Name, Logo, Flatlay, and V5 Mockup design of a new energy drink*
We are a current RTD (ready to drink) company looking to expand into the Energy market. We are not sure if we will stick with our parent company name or go a completely different direction. That's where you come in.
Get creative. Come up with a name, design a logo, and create the look and feel of our next big product. We want fun, bright, and forward-thinking designs. Don't think Zipfox and tundra, but more along the lines of Crane, V5, and Tilt as our proposed target market is in the same 18-25 demographic.
The only request is the Term "With Super Caffeine" appear somewhere on the visible label. A V5 can render is attached. Please provide a Lay Flat and a Rendered Can together when submitting your designs.
FYI, the design brief is just a generic template. DO NOT USE the "grunge" or "brick" as a reference when creating your designs. We are offering a $1,000 prize to the winning designer. So please, really think this through. 1 great design is better than 5 quick designs. Good Luck!
18-25

```html
<!DOCTYPE html>
<html lang="en">
<head>
<meta charset="utf-8">
<title>ZELO Energy Booster – Label Lay Flat</title>
<link href="https://fonts.googleapis.com/css2?family=Oswald:wght@500;700&family=Russo+One&family=Caveat:wght@500&display=swap" rel="stylesheet">
<style>
  :root {
    --magenta: #e02fb5;
    --magenta-deep: #b3178f;
    --orchid: #e36be0;
    --violet: #8a3fc4;
    --ink: #17161a;
    --charcoal: #3a393e;
    --sky: #3fc3f2;
    --azure: #1f7fd6;
    --sun: #ffd21a;
    --white: #ffffff;
  }
  * { margin: 0; padding: 0; box-sizing: border-box; }
  html, body { width: 1017px; height: 1200px; overflow: hidden; background: var(--magenta); }
  .label { display: block; width: 1017px; height: 1200px; }
  .claims { font-family: "Oswald", sans-serif; font-weight: 500; font-size: 34px; letter-spacing: 5px; fill: var(--white); }
  .brand-name { font-family: "Oswald", sans-serif; font-weight: 700; font-size: 300px; letter-spacing: 6px; fill: var(--white); }
  .tagline { font-family: "Caveat", cursive; font-weight: 500; font-size: 70px; }
  .stripe-title { font-family: "Russo One", sans-serif; font-size: 58px; letter-spacing: 2px; fill: var(--white); }
  .legal { font-family: "Oswald", sans-serif; font-weight: 500; font-size: 44px; fill: var(--white); }
</style>
</head>
<body>
<svg class="label" viewBox="0 0 1017 1200" xmlns="http://www.w3.org/2000/svg">
  <defs>
    <linearGradient id="body-fill" x1="0" y1="0" x2="1" y2="0">
      <stop offset="0" stop-color="var(--orchid)"/>
      <stop offset="0.55" stop-color="var(--magenta)"/>
      <stop offset="1" stop-color="var(--magenta-deep)"/>
    </linearGradient>
    <linearGradient id="band-fill" x1="0" y1="0" x2="1" y2="0">
      <stop offset="0" stop-color="var(--charcoal)"/>
      <stop offset="0.45" stop-color="#4a494f"/>
      <stop offset="1" stop-color="var(--ink)"/>
    </linearGradient>
    <linearGradient id="bolt-edge" x1="0" y1="0" x2="1" y2="0">
      <stop offset="0" stop-color="var(--violet)"/>
      <stop offset="0.6" stop-color="var(--sky)"/>
      <stop offset="1" stop-color="var(--azure)"/>
    </linearGradient>
    <linearGradient id="stripe-fill" x1="0" y1="0" x2="1" y2="0">
      <stop offset="0" stop-color="var(--sky)"/>
      <stop offset="1" stop-color="var(--azure)"/>
    </linearGradient>
    <linearGradient id="tagline-fill" x1="0" y1="0" x2="1" y2="0">
      <stop offset="0" stop-color="var(--sky)"/>
      <stop offset="0.5" stop-color="#f4a6e8"/>
      <stop offset="1" stop-color="var(--sky)"/>
    </linearGradient>
    <linearGradient id="halftone-top" x1="0" y1="0" x2="0" y2="1">
      <stop offset="0" stop-color="var(--sun)" stop-opacity="0.55"/>
      <stop offset="1" stop-color="var(--sun)" stop-opacity="0"/>
    </linearGradient>
    <linearGradient id="halftone-bottom" x1="0" y1="1" x2="0" y2="0">
      <stop offset="0" stop-color="var(--sun)" stop-opacity="0.5"/>
      <stop offset="1" stop-color="var(--sun)" stop-opacity="0"/>
    </linearGradient>
    <linearGradient id="base-violet" x1="0" y1="0" x2="0" y2="1">
      <stop offset="0" stop-color="var(--magenta)" stop-opacity="0"/>
      <stop offset="1" stop-color="var(--violet)"/>
    </linearGradient>
  </defs>

  <rect class="label-body" width="1017" height="1200" fill="url(#body-fill)"/>
  <rect class="label-base-glow" y="1000" width="1017" height="200" fill="url(#base-violet)"/>

  <rect class="halftone-top" width="1017" height="200" fill="url(#halftone-top)" role="img" aria-label="Yellow halftone dot texture fading down from the top edge"/>
  <rect class="halftone-bottom" y="1020" width="1017" height="180" fill="url(#halftone-bottom)" role="img" aria-label="Yellow halftone dot texture fading up from the bottom edge"/>

  <text class="claims" x="508" y="250" text-anchor="middle">BCAA AMINO   ·   SUPER CAFFEINE</text>

  <g class="energy-band">
    <polygon class="band-edge-top" points="0,400 770,250 700,330 1017,270 1017,300 690,372 760,290 0,445" fill="url(#bolt-edge)"/>
    <polygon class="band-core" points="0,445 760,290 690,372 1017,300 1017,760 610,850 670,770 0,890" fill="url(#band-fill)"/>
    <polygon class="band-stripe" points="0,890 670,770 610,850 1017,760 1017,800 590,905 650,830 0,985" fill="url(#stripe-fill)"/>
  </g>

  <text class="brand-name" x="508" y="690" text-anchor="middle">ZELO</text>
  <text class="tagline" x="508" y="790" text-anchor="middle" fill="url(#tagline-fill)">maximize your limits</text>

  <text class="stripe-title" x="60" y="948" transform="rotate(-10 60 948)">ENERGY BOOSTER</text>

  <text class="legal" x="508" y="1060" text-anchor="middle">Natural &amp; Artificial Flavors</text>
  <text class="legal" x="508" y="1115" text-anchor="middle">16 fl oz (1 PT) 473 ml</text>
</svg>
</body>
</html>
```